Beacon Lending. We focus on mentoring our clients into a home. Partner Beacon Realty Group

Needing a Mortgage Company Website. We would like a mortgage calculator on the site as well as it linked to our partner sites.

We have 6 Other Websites that go into this.

We focus on helping our clients get approved for a home. We would like a mortgage calculator on it.
See other sites
www.harborvalehomes.example
www.keystepready.example

Target Market(s)

Modern, Average guy.

Industry/Entity Type

Mortgage Brokerage

Number of Pages Required

4 page

Font styles to use
Serif
Sans Serif

Colors
000000
0255a3
33a6d7

Requirements
Must have
• Plugins, Calculator, nice design, Contact form, SEO capability, etc.
Nice to have
• Someone I can hire for our 547 other sites. Finding a good designer is difficult and we have about 3 years worth of work.
Should not have
• You can pick the colors. Just Had some ideas. Please feel free to adjust it to your liking, You are the pro..
• We just want a nice clean friendly site we can capture leads on. We want to link our other companies and also Provide them worth Education and Tools to get approved for loan

```html
<!DOCTYPE html>
<html lang="en">
<head>
<meta charset="utf-8">
<title>Beacon Lending</title>
<link rel="stylesheet" href="https://fonts.googleapis.com/css2?family=Raleway:wght@500;600;700;800&family=Open+Sans:wght@400;600;700&display=swap">
<style>
:root{
  --blue:#0255a3;
  --sky:#33a6d7;
  --black:#111111;
  --ink:#333333;
  --muted:#666666;
  --line:#c9c9c9;
  --white:#ffffff;
}
*{margin:0;padding:0;box-sizing:border-box}
html,body{width:1200px;height:3482px;overflow:hidden;background:var(--white)}
body{position:relative;font-family:"Open Sans",Arial,sans-serif;color:var(--ink)}
.abs{position:absolute}
.center{left:0;width:1200px;text-align:center}

/* hero */
.hero{position:absolute;left:0;top:0;width:1200px;height:650px;overflow:hidden}
.hero-photo{position:absolute;inset:0;background:linear-gradient(180deg,#0d3f86 0%,#2a5f9c 35%,#6f8fa6 55%,#4f6b3a 75%,#355226 100%)}
.hero-shade{position:absolute;inset:0;background:rgba(0,30,80,.25)}
.brand{position:absolute;left:111px;top:44px;display:flex;align-items:center;gap:14px;font-family:"Raleway",sans-serif;font-weight:800;font-size:34px;color:var(--white);letter-spacing:1px}
.brand-mark{width:22px;height:22px;background:var(--white)}
.nav{position:absolute;right:111px;top:54px;display:flex;gap:27px;font-family:"Raleway",sans-serif;font-weight:700;font-size:15px;color:var(--white)}
.nav .active{color:var(--sky)}
.nav svg{margin-top:1px}
.hero-title{top:195px;font-family:"Raleway",sans-serif;font-weight:700;font-size:60px;line-height:80px;color:var(--white)}
.hero-btn{position:absolute;left:490px;top:395px;width:220px;height:57px;border:2px solid var(--white);color:var(--white);font-family:"Open Sans",sans-serif;font-weight:700;font-size:16px;display:flex;align-items:center;justify-content:center}
.dots{position:absolute;left:560px;top:566px;display:flex;gap:6px}
.dots span{width:14px;height:14px;border-radius:50%;border:2px solid var(--white)}
.dots span.on{background:var(--white)}
.hero-cut{position:absolute;left:0;top:0}

/* headings */
.section-title{font-family:"Raleway",sans-serif;font-weight:700;font-size:37px;line-height:58px;color:var(--blue)}
.lead{font-size:15px;color:var(--muted)}

/* cards */
.card{position:absolute;top:1005px;width:304px;height:422px;background:var(--white);box-shadow:0 2px 8px rgba(0,0,0,.15);text-align:center}
.card.raised{box-shadow:0 8px 26px rgba(0,0,0,.25)}
.card-photo{position:relative;height:211px;overflow:hidden}
.card-photo svg{position:absolute;left:0;bottom:0}
.card h3{margin-top:42px;font-family:"Raleway",sans-serif;font-weight:600;font-size:23px;color:#222}
.card p{margin:16px auto 0;width:245px;font-size:13px;line-height:28px;color:var(--muted)}
.card a{display:block;margin-top:14px;font-weight:700;font-size:14px;color:var(--sky);text-decoration:none;letter-spacing:.5px}

/* calculator */
.calc-photo{position:absolute;left:0;top:1560px}
.calc-title{position:absolute;left:620px;width:432px;top:1603px;text-align:center;font-family:"Raleway",sans-serif;font-weight:800;font-size:37px;color:var(--blue)}
.calc-label{position:absolute;left:620px;font-size:16px;color:#444}
.calc-input{position:absolute;left:620px;width:432px;height:52px;border:1px solid #9a9a9a;padding-left:16px;display:flex;align-items:center;font-size:17px;color:#555}
.btn{position:absolute;display:flex;align-items:center;justify-content:center;background:var(--sky);color:var(--white);font-weight:700;font-size:16px;letter-spacing:.5px}

/* advantage */
.copy{font-size:15.5px;line-height:33px;color:var(--muted)}

/* footer */
.footer-shape{position:absolute;left:0;top:2920px}
.foot-brand{top:3080px;display:flex;justify-content:center;align-items:center;gap:14px;font-family:"Raleway",sans-serif;font-weight:700;font-size:38px;color:var(--white);letter-spacing:1px}
.foot-mark{width:24px;height:24px;background:var(--white)}
.social{position:absolute;left:487px;top:3248px;display:flex;gap:6px}
.social span{width:52px;height:52px;border-radius:50%;border:2px solid var(--white)}
.contact{top:3336px;display:flex;justify-content:center;align-items:center;gap:12px;font-size:15px;color:var(--white)}
.contact svg{fill:var(--white)}
.links{top:3373px;font-size:15px;color:var(--white);word-spacing:4px}
.copyright{top:3410px;font-size:15px;color:var(--white)}
</style>
</head>
<body>

<header class="hero">
  <div class="hero-photo" role="img" aria-label="Photo of a blue family house with a green lawn at dusk"></div>
  <div class="hero-shade"></div>
  <div class="brand"><span class="brand-mark"></span>Beacon Lending</div>
  <nav class="nav">
    <span class="active">HOME</span><span>ABOUT US</span><span>PROCESS</span><span>KEYSTEP READY</span><span>CONTACT US</span>
    <svg width="16" height="16" viewBox="0 0 16 16"><circle cx="6.5" cy="6.5" r="5" fill="none" stroke="#fff" stroke-width="2.2"/><line x1="10.5" y1="10.5" x2="15" y2="15" stroke="#fff" stroke-width="2.6"/></svg>
  </nav>
  <h1 class="abs center hero-title">FOCUS ON MENTORING<br>OUR CLIENTS INTO A HOME</h1>
  <div class="hero-btn">CONTACT US TODAY!</div>
  <div class="dots"><span class="on"></span><span></span><span></span><span></span></div>
  <svg class="hero-cut" width="1200" height="650" viewBox="0 0 1200 650">
    <polygon points="0,395 290,650 0,650" fill="#fff"/>
    <polygon points="1200,395 910,650 1200,650" fill="#fff"/>
    <polygon points="0,598 60,650 0,650" fill="var(--blue)"/>
    <polygon points="1200,598 1140,650 1200,650" fill="var(--blue)"/>
  </svg>
</header>

<h2 class="abs center section-title" style="top:765px">ARE YOU TRYING TO BUY A HOME? DID YOU SIT WITH<br>A LENDER OR BROKER AND GET DENIED?</h2>
<p class="abs center lead" style="top:912px">We understand your pain.&nbsp; They just pulled a hard inquiry on your credit profile just to damage in further.</p>

<article class="card" style="left:111px">
  <div class="card-photo" role="img" aria-label="Photo of a couple standing in front of a house" style="background:linear-gradient(160deg,#8a7a66,#b9a58a 45%,#6a7d4d)">
    <svg width="304" height="40" viewBox="0 0 304 40"><polygon points="0,0 40,40 0,40" fill="#fff"/><polygon points="304,0 264,40 304,40" fill="#fff"/><polygon points="0,24 16,40 0,40" fill="var(--blue)"/><polygon points="304,24 288,40 304,40" fill="var(--blue)"/></svg>
  </div>
  <h3>KeyStep Ready</h3>
  <p>Nam libero tempore, cum soluta nobest eligendi optio cumque nihil imp.</p>
  <a>GET STARTED</a>
</article>
<article class="card raised" style="left:448px">
  <div class="card-photo" role="img" aria-label="Photo of a hand signing a loan document" style="background:linear-gradient(150deg,#0d2c6a,#3d6fb0 50%,#c9d4e4)">
    <svg width="304" height="40" viewBox="0 0 304 40"><polygon points="0,0 40,40 0,40" fill="#fff"/><polygon points="304,0 264,40 304,40" fill="#fff"/><polygon points="0,24 16,40 0,40" fill="var(--blue)"/><polygon points="304,24 288,40 304,40" fill="var(--blue)"/></svg>
  </div>
  <h3>Loan Requirements</h3>
  <p>Nam libero tempore, cum soluta nobest eligendi optio cumque nihil imp.</p>
  <a>SEE YOUR OPTIONS</a>
</article>
<article class="card" style="left:784px">
  <div class="card-photo" role="img" aria-label="Photo of a couple meeting with an advisor" style="background:linear-gradient(160deg,#d9d6d0,#9d9a95 50%,#5e6266)">
    <svg width="304" height="40" viewBox="0 0 304 40"><polygon points="0,0 40,40 0,40" fill="#fff"/><polygon points="304,0 264,40 304,40" fill="#fff"/><polygon points="0,24 16,40 0,40" fill="var(--blue)"/><polygon points="304,24 288,40 304,40" fill="var(--blue)"/></svg>
  </div>
  <h3>Get Pre-Approved</h3>
  <p>Nam libero tempore, cum soluta nobest eligendi optio cumque nihil imp.</p>
  <a>READ MORE</a>
</article>

<svg class="calc-photo" width="1200" height="566" viewBox="0 0 1200 566" role="img" aria-label="Photo of a hand using a calculator beside a coffee cup">
  <defs>
    <linearGradient id="calcTone" x1="0" y1="0" x2="1" y2="1">
      <stop offset="0" stop-color="#f1f1ef"/><stop offset=".55" stop-color="#d4d6d8"/><stop offset="1" stop-color="#4a4c50"/>
    </linearGradient>
    <linearGradient id="cornerTone" x1="0" y1="0" x2="1" y2="1">
      <stop offset="0" stop-color="#e8dccb"/><stop offset="1" stop-color="#c7b59b"/>
    </linearGradient>
  </defs>
  <polygon points="0,0 348,0 657,566 0,566" fill="url(#calcTone)"/>
  <line x1="348" y1="0" x2="657" y2="566" stroke="#7fa6d6" stroke-width="4"/>
  <polygon points="1070,0 1200,0 1200,228" fill="url(#cornerTone)"/>
</svg>
<h2 class="calc-title">MORTGAGECALCULATOR</h2>
<div class="calc-label" style="top:1673px">Enter mortgage amount:</div>
<div class="calc-input" style="top:1713px">$</div>
<div class="calc-label" style="top:1777px">Length of mortgage term:</div>
<div class="calc-input" style="top:1817px">Years</div>
<div class="calc-label" style="top:1889px">Interest rate:</div>
<div class="calc-input" style="top:1929px">%</div>
<div class="btn" style="left:764px;top:2019px;width:157px;height:61px">CALCULATE</div>

<h2 class="abs center section-title" style="top:2255px">WOULDN’T YOU LIKE TO KNOW IF YOU CAN GET<br>APPROVED BEFORE YOU DAMAGE YOUR CREDIT ANYMORE?</h2>
<p class="abs center copy" style="top:2407px">Call Beacon Lending today and talk to one of our agents, we can do a full financial analysis, pull your credit file,<br>and figure out your DTI before you speak with a lender or broker.</p>
<p class="abs center copy" style="top:2505px">We also have an advantage!&nbsp; We work with every different lender/broker so we can offer you every<br>program out there. Not just ones that are partners or let say “prefered vendors”</p>
<p class="abs center copy" style="top:2602px">Sit with Beacon Lending today!&nbsp; Let us worry about getting you approved before you waste you time/money<br>and damage your credit any further!</p>
<div class="btn" style="left:499px;top:2720px;width:202px;height:63px">FIND AN LENDER</div>

<svg class="footer-shape" width="1200" height="562" viewBox="0 0 1200 562">
  <rect x="0" y="0" width="1200" height="562" fill="var(--black)"/>
  <polygon points="0,0 70,0 330,260 0,260" fill="#fff"/>
  <polygon points="1200,0 1130,0 870,260 1200,260" fill="#fff"/>
  <rect x="0" y="255" width="1200" height="307" fill="var(--black)"/>
  <polygon points="0,260 330,260 0,0" fill="#fff" opacity="0"/>
  <polygon points="0,0 60,0 0,56" fill="var(--blue)"/>
  <polygon points="1200,0 1140,0 1200,56" fill="var(--blue)"/>
</svg>
<div class="abs center foot-brand"><span class="foot-mark"></span>KeyStep Ready</div>
<div class="social"><span></span><span></span><span></span><span></span></div>
<div class="abs center contact">
  <svg width="12" height="16" viewBox="0 0 12 16"><path d="M6 0a6 6 0 0 0-6 6c0 4.5 6 10 6 10s6-5.5 6-10a6 6 0 0 0-6-6zm0 8.5A2.5 2.5 0 1 1 6 3.5a2.5 2.5 0 0 1 0 5z"/></svg>
  <span>1420 Harbor Point Rd Fairview, VA 22190</span><span>|</span>
  <svg width="15" height="15" viewBox="0 0 16 16"><path d="M3.6 1l2.5 3.2-1.5 1.8a9.5 9.5 0 0 0 5.4 5.4l1.8-1.5L15 12.4 13.4 15C6.8 14.8 1.2 9.2 1 2.6z"/></svg>
  <span>1 800 555 0142</span><span>|</span>
  <svg width="17" height="13" viewBox="0 0 17 13"><path d="M0 0h17v1.5L8.5 7 0 1.5zM0 3.3l8.5 5.4L17 3.3V13H0z"/></svg>
  <span>info@beaconlending.example</span>
</div>
<p class="abs center links">Help &nbsp;| &nbsp;FAQ &nbsp;| &nbsp;Support &nbsp;| &nbsp;Sitemap &nbsp;| &nbsp;Terms Of Use &nbsp;| &nbsp;Privacy Statement</p>
<p class="abs center copyright">Beacon Lending © 2019 All rights reserved.</p>

</body>
</html>
```